Film Company needs Poster Design Project for upcoming film "VANE"

At Brindlewood Films, we need a poster design for our upcoming feature film project "VANE," America first 'rock and roll' star. Our film will cover Tobias Merrick Vane's life his drinking, passion and writing. It will not be a horror film, but rather a biopic on his life.
Brindlewood Films is a full service film and television production company, founded by Curtis Belmont and Quarnet, LLC in 2006. Brindlewood Films’ mission is to blend artistic talent with engaging stories to create feature films and television that delight audiences of all ages.
We would like to see designs that embody Tobias Merrick Vane as a person. The film will cover most of his famous poems/novels/short stories so any reference to "Hollow lantern" or "The Quill Moth," etc...would work.
Updates
Thank you ALL for the amazing work you have submitted, you made it really hard for me to come up with one choice. I will make my decision by Wednesday.
Target Market(s)
Target audience 18 - 35
Industry/Entity Type
It Company
Look and feel

```html
<!DOCTYPE html>
<html lang="en">
<head>
<meta charset="utf-8">
<title>VANE — Brindlewood Films</title>
<link href="https://fonts.googleapis.com/css2?family=Cormorant:wght@400;500&family=Oswald:wght@400;500;600&family=Montserrat:wght@500;600&display=swap" rel="stylesheet">
<style>
  :root {
    --bg: #2e2118;
    --panel: #5b5a1c;
    --panel-glow: #c8c46a;
    --frame: #a9a89c;
    --rust: #7a2b16;
    --ink: #111008;
    --olive-text: #8c8a34;
    --badge-top: #8a3e1c;
    --badge-bottom: #c8784a;
    --logo-box: #a8a8a8;
    --logo-name: #e0a021;
    --url: #e8e4d8;
  }
  * { margin: 0; padding: 0; box-sizing: border-box; }
  html, body { width: 900px; height: 1200px; overflow: hidden; background: var(--bg); }
  .poster { position: relative; width: 900px; height: 1200px; background: var(--bg); overflow: hidden; }

  .bird-art { position: absolute; left: 0; top: 10px; width: 282px; height: 140px; }

  .stage {
    position: absolute; left: 113px; top: 140px; width: 680px; height: 662px;
    background: radial-gradient(ellipse 70% 18% at 50% 100%, var(--panel-glow) 0%, rgba(200,196,106,0) 100%), var(--panel);
    box-shadow: inset 0 0 0 3px rgba(0,0,0,.35), inset 4px 4px 6px rgba(0,0,0,.5), 2px 3px 8px rgba(0,0,0,.6);
  }

  .frame { position: absolute; background: var(--frame); padding: 18px; box-shadow: 2px 3px 6px rgba(0,0,0,.5); }
  .frame .art { width: 100%; height: 100%; }
  .frame--left { left: 37px; top: 10px; width: 262px; height: 300px; transform: rotate(-1.5deg); }
  .frame--left .art { background: radial-gradient(ellipse at 50% 40%, #d8d49a 0%, #6e6a2e 55%, #1e1c0c 100%); }
  .frame--right { left: 378px; top: 48px; width: 258px; height: 332px; transform: rotate(1.5deg); }
  .frame--right .art { background: radial-gradient(ellipse at 50% 65%, #f3c8a0 0%, #a8562a 50%, #3a1408 100%); }

  .presents {
    position: absolute; left: 100px; top: 315px; width: 200px;
    font-family: "Oswald", sans-serif; font-weight: 400; font-size: 34px; line-height: 1.05;
    color: var(--rust); text-align: center; text-transform: uppercase;
  }
  .presents span { display: block; }
  .presents .line-two { padding-left: 60px; }

  .title {
    position: absolute; left: 66px; top: 350px;
    font-family: "Cormorant", serif; font-weight: 500; font-size: 300px; line-height: 1;
    color: var(--ink); letter-spacing: -4px; white-space: nowrap;
    transform: scaleX(.45); transform-origin: left top;
    text-shadow: 2px 3px 4px rgba(0,0,0,.4);
  }

  .badge {
    position: absolute; left: 412px; top: 418px; width: 262px; height: 148px;
    background: linear-gradient(180deg, var(--badge-top) 0%, var(--badge-bottom) 60%, #5c2410 100%);
    border: 2px solid #2a1208; box-shadow: inset 0 0 0 4px rgba(255,200,150,.25);
    display: flex; align-items: center; justify-content: center; text-align: center;
    font-family: "Montserrat", sans-serif; font-weight: 600; font-size: 23px; line-height: 1.3;
    color: var(--ink); text-transform: uppercase;
  }

  .works {
    position: absolute; left: 128px; top: 764px;
    font-family: "Oswald", sans-serif; font-weight: 500; font-size: 17px;
    color: var(--ink); text-transform: uppercase; white-space: nowrap; letter-spacing: -.2px;
    transform: scaleX(.95); transform-origin: left top;
  }

  .tagline {
    position: absolute; left: 0; top: 812px; width: 900px; text-align: center;
    font-family: "Oswald", sans-serif; font-weight: 600; font-size: 48px; line-height: 1.2;
    color: var(--rust); text-transform: uppercase; letter-spacing: -1px; white-space: nowrap;
    transform: scaleX(.8); transform-origin: center top;
  }
  .subline {
    position: absolute; left: 0; top: 900px; width: 900px; text-align: center; padding-right: 20px;
    font-family: "Montserrat", sans-serif; font-weight: 600; font-size: 33px; white-space: nowrap;
    color: var(--ink); text-transform: uppercase;
  }

  .release {
    position: absolute; left: 80px; top: 1030px;
    font-family: "Oswald", sans-serif; font-weight: 500; font-size: 94px; line-height: 1;
    color: var(--olive-text); text-transform: uppercase; letter-spacing: 2px;
  }

  .studio { position: absolute; left: 698px; top: 963px; width: 172px; }
  .studio__mark {
    width: 172px; height: 192px; background: var(--logo-box);
    display: flex; align-items: center; justify-content: center; text-align: center;
    font-family: "Oswald", sans-serif; font-weight: 600; font-size: 22px; line-height: 1.1;
    color: var(--logo-name); text-transform: uppercase;
  }
  .studio__url {
    margin-top: 6px; text-align: center;
    font-family: "Montserrat", sans-serif; font-weight: 500; font-size: 10px;
    color: var(--url); text-transform: uppercase; letter-spacing: .3px;
  }
</style>
</head>
<body>
<main class="poster">
  <svg class="bird-art" viewBox="0 0 282 140" role="img" aria-label="Silhouette of a black bird perched on the top edge of the panel">
    <rect x="0" y="0" width="282" height="140" rx="40" fill="#141010"/>
  </svg>

  <section class="stage">
    <figure class="frame frame--left">
      <div class="art" role="img" aria-label="Sepia portrait photograph of Tobias Merrick Vane"></div>
    </figure>
    <figure class="frame frame--right">
      <div class="art" role="img" aria-label="Inverted orange-toned portrait of Tobias Merrick Vane"></div>
    </figure>

    <p class="presents"><span>Brindlewood</span><span class="line-two">Presents</span></p>
    <h1 class="title">VANE</h1>
    <p class="badge">America’s first<br>‘Rock and roll’<br>star</p>
  </section>

  <p class="works">Covering some of his best works including ‘The Quill Moth’ ‘Hollow Lantern’ &amp; The Ashen Hound</p>
  <h2 class="tagline">A biopic on the life of Tobias Merrick Vane</h2>
  <p class="subline">His drinking, passion and writing</p>

  <p class="release">Coming Soon</p>

  <aside class="studio">
    <div class="studio__mark">Brindlewood<br>Films</div>
    <p class="studio__url">www.brindlewoodfilms.com</p>
  </aside>
</main>
</body>
</html>
```